Graphic to show easy steps to find financial clarity

Howdy-I need a graphic that describe my Coin Compass Method.The attached is a concept, but please use your own creativity to show how you would display this:- There are 5 steps the process (and then we repeat/recalculate)- And three bullets that drive home the results of the processI've also attached my logo. Please use the colors in my logo and maybe add a soft green as needed.The reader should be able to briefly scan this document and understand that this is an easy/simple process that tells them how to manage their cash.Thanks!-Ned

Target Market(s)

wealthy women, whether single or married

Requirements
Must have
• Please use the colors in my logo and a soft green if needed
Should not have
• This should be a very easy to read graphic that communicates how simple/easy this is to do.

```html
<!DOCTYPE html>
<html lang="en">
<head>
<meta charset="utf-8">
<title>Coin Compass Method</title>
<link rel="stylesheet" href="https://fonts.googleapis.com/css2?family=Bebas+Neue&family=Tinos:wght@400&display=swap">
<style>
  :root {
    --navy: #0c3a80;
    --slate: #6a6a6a;
    --ink: #1e1e1e;
    --paper: #ffffff;
    --bracket: 16px;
  }
  * { margin: 0; padding: 0; box-sizing: border-box; }
  html, body { width: 1200px; height: 811px; overflow: hidden; background: var(--paper); }
  .canvas { position: relative; width: 1200px; height: 811px; font-family: "Tinos", "Times New Roman", serif; color: var(--ink); }

  .brand { position: absolute; left: 166px; top: 180px; display: flex; align-items: center; gap: 12px; }
  .brand-mark { width: 40px; height: 40px; background: var(--slate); }
  .brand-name { font-family: "Tinos", serif; font-size: 30px; color: var(--navy); letter-spacing: 0.5px; }

  .title { position: absolute; left: 165px; top: 236px; font-family: "Bebas Neue", sans-serif; font-size: 41px; color: var(--navy); letter-spacing: 0.5px; line-height: 1; }

  .step-label { position: absolute; font-family: "Bebas Neue", sans-serif; font-size: 38px; line-height: 1; letter-spacing: 1px; }
  .step-label.blue { color: var(--navy); }
  .step-label.gray { color: var(--slate); }

  .corner { position: absolute; width: 24px; height: 24px; }

  .bracket { position: absolute; width: 141px; height: 102px; border-top: var(--bracket) solid; border-left: var(--bracket) solid; }
  .bracket.blue { border-color: var(--navy); }
  .bracket.gray { border-color: var(--slate); }
  .bracket p { position: absolute; left: 5px; top: 8px; font-size: 20px; line-height: 24px; width: 130px; }

  .repeat-bar { position: absolute; left: 951px; top: 286px; width: 124px; height: 16px; background: var(--slate); }
  .repeat-text { position: absolute; left: 951px; top: 311px; width: 124px; text-align: center; font-size: 20px; line-height: 24px; }

  .outcomes { position: absolute; left: 0; top: 0; }
  .timeline { position: absolute; left: 420px; top: 530px; }
  .outcome { position: absolute; top: 588px; width: 200px; text-align: center; font-size: 18px; line-height: 22px; }
</style>
</head>
<body>
<main class="canvas">
  <header>
    <div class="brand"><span class="brand-mark"></span><span class="brand-name">Harlow Wealth Group</span></div>
    <h1 class="title">COIN COMPASS METHOD</h1>
  </header>

  <section class="steps">
    <div class="step-label blue" style="left:184px; top:405px;">Step 1</div>
    <svg class="corner" style="left:275px; top:411px;" viewBox="0 0 24 24"><polygon points="0,24 24,0 24,24" fill="var(--navy)"/></svg>
    <div class="bracket blue" style="left:158px; top:452px;"><p>Know your annual spending</p></div>

    <div class="step-label gray" style="left:350px; top:364px;">Step 2</div>
    <svg class="corner" style="left:436px; top:370px;" viewBox="0 0 24 24"><polygon points="0,24 24,0 24,24" fill="var(--slate)"/></svg>
    <div class="bracket gray" style="left:319px; top:411px;"><p>Project special expenses</p></div>

    <div class="step-label blue" style="left:512px; top:322px;">Step 3</div>
    <svg class="corner" style="left:596px; top:328px;" viewBox="0 0 24 24"><polygon points="0,24 24,0 24,24" fill="var(--navy)"/></svg>
    <div class="bracket blue" style="left:478px; top:370px;"><p>Add up your 5-year cash needs</p></div>

    <div class="step-label gray" style="left:666px; top:284px;">Step 4</div>
    <svg class="corner" style="left:757px; top:286px;" viewBox="0 0 24 24"><polygon points="0,24 24,0 24,24" fill="var(--slate)"/></svg>
    <div class="bracket gray" style="left:639px; top:328px;"><p>Set them aside in savings</p></div>

    <div class="step-label blue" style="left:837px; top:241px;">Step 5</div>
    <div class="bracket blue" style="left:800px; top:286px;"><p>Invest the rest</p></div>

    <div class="step-label blue" style="left:973px; top:241px;">Repeat</div>
    <div class="repeat-bar"></div>
    <p class="repeat-text">Recalculate monthly</p>
  </section>

  <section class="outcomes">
    <svg class="timeline" width="500" height="50" viewBox="0 0 500 50">
      <defs>
        <radialGradient id="knob" cx="0.35" cy="0.3" r="0.8">
          <stop offset="0" stop-color="#9a9a9a"/>
          <stop offset="0.6" stop-color="#6a6a6a"/>
          <stop offset="1" stop-color="#4a4a4a"/>
        </radialGradient>
      </defs>
      <line x1="4" y1="23" x2="494" y2="23" stroke="var(--navy)" stroke-width="8" stroke-linecap="round"/>
      <circle cx="40" cy="23" r="22" fill="url(#knob)"/>
      <circle cx="246" cy="23" r="22" fill="url(#knob)"/>
      <circle cx="450" cy="23" r="22" fill="url(#knob)"/>
    </svg>
    <p class="outcome" style="left:360px;">Know your lifestyle will be unaffected by the markets for at least 5 years.</p>
    <p class="outcome" style="left:566px; top:591px;">Spend intentionally and with joy</p>
    <p class="outcome" style="left:766px; top:592px;">Create a solid base for lifetime cash flow projections</p>
  </section>
</main>
</body>
</html>
```